Beauty Salon Industry - Web Design Project

zQuarta is a well-funded start up developing an Online Marketing Platform for small businesses in Europe.
We require a large number of high quality business web designs for our business website builder. Our business websites are seamlessly integrated into our Online Marketing systems and therefore it is important for designers to comply with our Design Guidelines.
This is our second contest and it will focus on the beauty salon industry. We will be running contents every 2-3 weeks for a new industry. Last month, we ran a contest for Builder website designs with 3 top prizes (plus £10 per variation) and we also paid out £25 per design for 20+ entries from designers who did not win the top prizes. So we encourage all entries!
We have included a wire frame this time to encourage you to be as creative as possible with your designs and layout while respecting the following guidelines:
1) You CAN change the layout as much as you like. If you think a vertical menu would look better, then use it. If you think the design would benefit from moving an element to a different location, then you can do that too.
2) You must include ALL the elements in the wire frame in your design.(e.g. latest 2 news entries, a testimonial, 1 gallery image, carousel etc...). Please make sure you have looked through the wire frame and know what is required. Entries that do not include all the elements will not qualify to win.
3) So remember, you CAN change the layout as much as you like but DO NOT remove any elements nor move them to a different page.
4) You may change the size and style of the carousel image. We would like to see as many variations of this as possible.
We are rewarding 3 prizes, and would like the winning designer to design the internal pages to the new design.
As always, if we think your designs could be incorporated into our system, but you do not win the competition, we will reward £25. Therefore, we encourage designers to submit as many designs as possible as we may award up to 25 designs.
Judging criteria : -
1) Visual Design
2) Layout must adhere to best practices and wireframe. If you decide to move elements around significantly please provide reason
3) Functional, informative and drives calls to action
Updates
As usual:
1st place = £350
2nd place = £250
3rd place = £150
Good luck!
Very happy with all the designs submitted so far, and will provide feedback ASAP.
We would like to see you try arranging the elements differently. So please try different navigation types and layouts.
Thanks
Morris
Prize funds for 1st place has been slightly increased.
Thanks
Morris
We have already had some amazing designs submitted. Thanks.
Remember to play with the layout of the elements and try designs with a carousel/slider that is in portrait not just in landscape.
Thanks everyone!
Morris
Hi everyone, we are really enjoying looking through the designs.
We have one NEW requirement. If you have used an image from http://www.frelik-example.com/ in your design, could you please replace it with another.
We are not associated with them.
Thank you.
I have just sent a poll around the office to vote on all the designs and hope to have the results soon.
Good luck and I hope to see all your great designs for our next project in a couple of weeks.
Morris
Hi everyone, we hope you have had a good holiday season. We will be rewarding the prizes very soon, hopefully today or tomorrow.
Thanks
Morris
We are currently going through all the designs that did not win our competition and will be contacting the designers of the designs we would like to use in our system, so please keep an eye on your inbox over the next few days.
Thank you
Morris
Target Market(s)
Beauty Salon Industry
Industry/Entity Type
Beauty Salon
Look and feel
Each slider illustrates characteristics of the customer's brand and the style your logo design should communicate.

```html
<!DOCTYPE html>
<html lang="en">
<head>
<meta charset="utf-8">
<title>Velvet Mane – hair and urban spa</title>
<link rel="stylesheet" href="https://fonts.googleapis.com/css2?family=Arimo:wght@400;700&family=Lora:ital,wght@0,400;1,400;1,700&family=PT+Sans:wght@400;700&display=swap">
<style>
:root{
  --berry:#b3244f;
  --berry-dark:#8c1a3e;
  --berry-light:#cf4a73;
  --ink:#333;
  --muted:#777;
  --soft:#999;
  --line:#ddd;
  --panel:#f1f1f1;
  --page:#fff;
  --sans:"PT Sans",sans-serif;
  --body:"Arimo",sans-serif;
  --serif:"Lora",serif;
}
*{box-sizing:border-box;margin:0;padding:0}
html,body{width:1200px;height:960px;overflow:hidden;background:var(--page)}
body{position:relative;font-family:var(--body);color:var(--ink)}
.abs{position:absolute}

/* header */
.site-header{left:0;top:0;width:1200px;height:87px;background:linear-gradient(#fff,#f4f4f4)}
.brand{left:120px;top:22px}
.brand-name{font-family:var(--sans);font-size:26px;font-weight:700;color:#8a8a8a;line-height:1}
.brand-tag{font-family:var(--sans);font-size:13px;color:#8a8a8a;margin-top:3px}
.phone{right:131px;top:17px;font-family:var(--sans);font-size:20px;color:#888;display:flex;align-items:center;gap:8px}
.btn{display:inline-flex;align-items:center;justify-content:center;border-radius:13px;color:#fff;font-family:var(--sans);font-size:13px;background:linear-gradient(var(--berry-light),var(--berry-dark));border:1px solid #7a1535;box-shadow:0 1px 2px rgba(0,0,0,.25)}
.btn-book{left:977px;top:45px;width:92px;height:23px;font-size:12px}
.hero-band{left:0;top:87px;width:1200px;height:47px;background:linear-gradient(var(--berry-light),var(--berry) 55%,var(--berry-dark));box-shadow:0 6px 10px -4px rgba(0,0,0,.25)}

/* menu */
.menu-panel{left:137px;top:178px;width:177px;height:276px;background:linear-gradient(#fafafa,#ececec);border:1px solid #d6d6d6}
.menu-ribbon{left:120px;top:171px}
.menu-list{list-style:none;left:137px;top:241px;width:177px;text-align:center;font-family:var(--sans);font-size:16px;color:#888}
.menu-list li{height:24.4px}

/* section headings */
.section-title{font-family:var(--serif);font-style:italic;font-size:14px;color:#444;display:flex;align-items:center;gap:10px}
.section-title::after{content:"";flex:1;height:8px;background:repeating-linear-gradient(135deg,#ddd 0 1px,transparent 1px 4px)}

/* gallery */
.gallery-title{left:121px;top:494px;width:210px}
.thumb{width:78px;height:66px;background:#fff;border:1px solid #ddd;padding:3px;box-shadow:0 1px 3px rgba(0,0,0,.15)}
.thumb span{display:block;width:100%;height:100%;background:linear-gradient(135deg,#e9c6a6,#b58363)}
.btn-see{left:180px;top:700px;width:92px;height:25px}

/* carousel */
.carousel{left:352px;top:172px;width:238px;height:381px;background:#fff;border:1px solid #ddd;box-shadow:0 8px 12px -6px rgba(0,0,0,.3)}
.carousel-photo{left:9px;top:10px;width:219px;height:361px;background:linear-gradient(160deg,#c2303f 0%,#9a4a3a 30%,#d7a184 60%,#e8d8cf 100%)}
.carousel-arrow{top:185px}

/* intro */
.intro{left:614px;top:168px;width:240px}
.intro h1{font-family:var(--serif);font-style:italic;font-weight:400;font-size:13.5px;line-height:19px;color:#333;margin-bottom:12px}
.intro p{font-size:12.4px;line-height:18.8px;color:#444;margin-bottom:9px}
.btn-dark{left:614px;top:391px;width:94px;height:24px;background:linear-gradient(#555,#1d1d1d);border-color:#111;font-family:var(--body);font-size:12px}

/* testimonial */
.testimonial-title{left:614px;top:445px;width:238px}
.quote{left:614px;top:476px;width:238px;text-align:center;font-family:var(--serif);font-style:italic;font-size:13.5px;line-height:19px;color:#888}
.quote-author{margin-top:8px;font-style:normal}

/* offer */
.offer{left:872px;top:172px;width:208px;height:268px}
.offer-box{left:0;top:0;width:208px;height:243px;border:1px solid #ddd;background:linear-gradient(#fff,#eee)}
.offer-image{left:9px;top:10px;width:189px;height:112px;background:linear-gradient(135deg,#f1b12a,#c9261d 55%,#8fd12a)}
.offer-price{left:0;top:130px;width:208px;text-align:center;font-family:var(--serif);font-style:italic;font-weight:700;font-size:30px;color:var(--berry)}
.offer-note{left:0;top:168px;width:208px;text-align:center;font-family:var(--serif);font-style:italic;font-size:15px;line-height:19px;color:#444}
.offer-ribbon{left:-1px;top:220px}
.offer-ribbon-label{left:0;top:225px;width:208px;text-align:center;font-family:var(--serif);font-style:italic;font-size:24px;color:#fff}

/* address */
.address{left:872px;top:464px;width:210px}
.address h2{font-family:var(--serif);font-style:italic;font-weight:400;font-size:13.5px;color:#333;margin-bottom:12px}
.address p{font-size:12.4px;line-height:18.8px;color:#444}
.map-link{display:block;margin-top:9px;font-family:var(--serif);font-style:italic;font-weight:700;font-size:13px;color:var(--berry);text-decoration:none}

/* news */
.news-title{left:353px;top:605px;width:498px}
.news-item{top:635px;width:240px}
.news-item h3{font-size:12.8px;font-weight:700;color:#222;margin-bottom:4px}
.news-item p{font-size:11.2px;line-height:18.8px;color:#444}
.news-item time{display:block;margin-top:2px;font-family:var(--serif);font-style:italic;font-size:10px;color:#aaa}
.btn-news{left:352px;top:746px;width:92px;height:25px}

/* hours */
.hours-title{left:871px;top:606px;width:209px}
.hours{left:872px;top:638px;border-collapse:collapse;font-size:12.4px;color:#222}
.hours th{text-align:left;font-weight:700;width:99px;height:16.9px;padding:0}
.hours td{padding:0}

/* partners */
.partners{left:0;top:806px;width:1200px;height:111px;border-top:1px dotted #ccc;background:linear-gradient(#fafafa,#ececec)}
.partner{top:42px;font-family:var(--sans);font-size:34px;color:#8f8f8f;letter-spacing:.5px}

/* footer */
.site-footer{left:0;top:917px;width:1200px;height:43px;background:linear-gradient(var(--berry-light),var(--berry) 50%,var(--berry-dark));font-family:var(--sans);font-size:12.5px;color:#fff}
.footer-links{right:130px;top:13px;display:flex;gap:14px}
.footer-links b{font-weight:700}
</style>
</head>
<body>

<header class="site-header abs">
  <div class="brand abs">
    <div class="brand-name">Velvet Mane</div>
    <div class="brand-tag">hair and urban spa</div>
  </div>
  <div class="phone abs">
    <svg width="14" height="20" viewBox="0 0 14 20" aria-hidden="true"><path d="M10 1 L13 5 L9 8 Q7 10 9 13 L12 15 L9 19 Q2 16 3 8 Q4 2 10 1Z" fill="#b3244f"/></svg>
    070 - 5550 - 0142
  </div>
  <a class="btn btn-book abs">BOOK NOW</a>
</header>
<div class="hero-band abs"></div>

<nav>
  <div class="menu-panel abs"></div>
  <svg class="menu-ribbon abs" width="212" height="54" viewBox="0 0 212 54" aria-hidden="true">
    <path d="M0 12 H32 V48 H0 L12 30Z" fill="#8c1a3e"/>
    <path d="M212 12 H180 V48 H212 L200 30Z" fill="#8c1a3e"/>
    <path d="M20 48 L32 42 V48Z" fill="#5e0f29"/>
    <path d="M192 48 L180 42 V48Z" fill="#5e0f29"/>
    <defs><linearGradient id="rib" x1="0" y1="0" x2="0" y2="1"><stop offset="0" stop-color="#cf4a73"/><stop offset="1" stop-color="#8c1a3e"/></linearGradient></defs>
    <rect x="30" y="0" width="152" height="44" fill="url(#rib)"/>
    <text x="106" y="29" text-anchor="middle" font-family="PT Sans, sans-serif" font-size="16" fill="#fff">MENU</text>
  </svg>
  <ul class="menu-list abs">
    <li>Home</li><li>Services</li><li>Gallery</li><li>Testimonials</li><li>News</li><li>About Us</li><li>Contact Us</li>
  </ul>
</nav>

<section>
  <h2 class="section-title gallery-title abs">Gallery</h2>
  <div class="thumb abs" style="left:141px;top:531px"><span role="img" aria-label="Back massage treatment"></span></div>
  <div class="thumb abs" style="left:233px;top:531px"><span role="img" aria-label="Relaxing facial treatment"></span></div>
  <div class="thumb abs" style="left:141px;top:612px"><span role="img" aria-label="Hand massage treatment"></span></div>
  <div class="thumb abs" style="left:233px;top:612px"><span role="img" aria-label="Spa client resting"></span></div>
  <a class="btn btn-see abs">See More</a>
</section>

<section class="carousel abs">
  <div class="carousel-photo abs" role="img" aria-label="Salon model with vivid red styled hair"></div>
  <svg class="carousel-arrow abs" style="left:-2px" width="26" height="36" viewBox="0 0 26 36" aria-hidden="true"><path d="M0 0 A18 18 0 0 1 0 36Z" fill="#fff"/><path d="M14 11 L6 18 L14 25Z" fill="#111"/></svg>
  <svg class="carousel-arrow abs" style="left:214px" width="26" height="36" viewBox="0 0 26 36" aria-hidden="true"><path d="M26 0 A18 18 0 0 0 26 36Z" fill="#fff"/><path d="M12 11 L20 18 L12 25Z" fill="#111"/></svg>
</section>

<section class="intro abs">
  <h1>LET OUR HAIR AND BEAUTY<br>SKILL BLOW YOU AWAY</h1>
  <p>Velvet Mane is a passionate, creative team, dedicated to delivering a second to none, personal salon experience that will ‘blow’ your mind</p>
  <p>Where ultimate hairdressing comes hand-in-hand with style, glamour, fashion, innovation and skill to create exquisite salon experience in the heart of London</p>
</section>
<a class="btn btn-dark abs">Read More</a>

<section>
  <h2 class="section-title testimonial-title abs">What They Say</h2>
  <blockquote class="quote abs">
    My hairstylist, Sienna, was<br>truly amazing. She listened to<br>exactly what I wanted,<br>but also told me exactly what...
    <div class="quote-author">- Maya Ellison -</div>
  </blockquote>
</section>

<aside class="offer abs">
  <div class="offer-box abs"></div>
  <div class="offer-image abs" role="img" aria-label="Red gift box with green ribbon"></div>
  <div class="offer-price abs">$25</div>
  <div class="offer-note abs">Complimentary gift for<br>first-time clients</div>
  <svg class="offer-ribbon abs" width="210" height="50" viewBox="0 0 210 50" aria-hidden="true">
    <path d="M0 10 H28 V46 H0 L10 28Z" fill="#8c1a3e"/>
    <path d="M210 10 H182 V46 H210 L200 28Z" fill="#8c1a3e"/>
    <defs><linearGradient id="rib2" x1="0" y1="0" x2="0" y2="1"><stop offset="0" stop-color="#cf4a73"/><stop offset="1" stop-color="#8c1a3e"/></linearGradient></defs>
    <rect x="26" y="0" width="158" height="42" fill="url(#rib2)"/>
  </svg>
  <div class="offer-ribbon-label abs">Book Now</div>
</aside>

<address class="address abs" style="font-style:normal">
  <h2>SALON ADDRESS :</h2>
  <p>12 Marlow Lane<br>London<br>W2 4QT</p>
  <a class="map-link">view map</a>
</address>

<section>
  <h2 class="section-title news-title abs">Latest News &amp; Insight</h2>
  <article class="news-item abs" style="left:352px">
    <h3>Book Now For Christmas</h3>
    <p>Our salon is usually very busy for the two weeks before Christmas, so please book early: call 020-5550-0187 or contact us</p>
    <time>December 4 2011</time>
  </article>
  <article class="news-item abs" style="left:614px">
    <h3>Book Now For Christmas</h3>
    <p>Our salon is usually very busy for the two weeks before Christmas, so please book early: call 020-5550-0187 or contact us</p>
    <time>December 4 2011</time>
  </article>
  <a class="btn btn-news abs">More News</a>
</section>

<section>
  <h2 class="section-title hours-title abs">Business Hours</h2>
  <table class="hours abs">
    <tr><th>Monday</th><td>8:30 - 5:30</td></tr>
    <tr><th>Tuesday</th><td>8:30 - 6:00</td></tr>
    <tr><th>Wednesday</th><td>8:30 - 6:00</td></tr>
    <tr><th>Thursday</th><td>8:30 - 6:00</td></tr>
    <tr><th>Friday</th><td>8:30 - 6:00</td></tr>
    <tr><th>Saturday</th><td>7:00 - 1:00</td></tr>
    <tr><th>Sunday</th><td>Closed</td></tr>
  </table>
</section>

<section class="partners abs">
  <span class="partner abs" style="left:140px">Lumière</span>
  <span class="partner abs" style="left:340px">Aveline</span>
  <span class="partner abs" style="left:582px">Corvin Hart</span>
  <span class="partner abs" style="left:920px">Dermeo</span>
</section>

<footer class="site-footer abs">
  <div class="footer-links abs"><span>Managed by <b>zQuarta</b></span><span>|</span><b>Admin</b></div>
</footer>

</body>
</html>
```